依頼概要
■依頼の目的/概要
コンサルティング業の中で「ほたる相談室」というテーマの中で、
営業力や対人対応力の向上支援などをお手伝いしています。
今回電子書籍出版にあたり、添付ファイルの書籍のイメージに沿うデザインを製作依頼させていただきます。

■書籍タイトル:『どうして?腕時計を磨くと来店客がふえるのか』
サブタイトル:「未来をひらくのは話術より笑顔力」

■本の内容
見た目が人に与える印象などについて記載したものになります。
営業マンのような個人の方や、法人教育に携わるような方にもお読みいただきたいものです。
詳細は添付ファイルを参照ください。

■デザイン要望
自由なご提案をおまちしております。
堅苦しくなく、気軽に手に取っていただけるようなデザインを希望です。

その他何かご不明な点がございましたら、お気軽にご質問下さい。
よろしくお願いいたします。
提案して頂いた皆様、私のミスで写真を2枚お送りできていませんでした。
大変申し訳ございませんがこの写真2枚を使って頂けますよう宜しくお願い致します。

この写真を使ってください
■ 選んだ理由

ネクタイの縦とメッセージの流れがとても良かったです。

■ 提案者全員のお礼・コメント

今回は、沢山の人にいろいろなデザインでご提案いただきありがとうございました。

```html
<!DOCTYPE html>
<html lang="ja">
<head>
<meta charset="utf-8">
<title>どうして?腕時計を磨くと来店客がふえるのか</title>
<link rel="stylesheet" href="https://fonts.googleapis.com/css2?family=Noto+Sans+JP:wght@500;700;900&family=Noto+Serif+JP:wght@500;700&display=swap">
<style>
  :root {
    --ink-dark: #0d0e12;
    --suit-grey: #3a3c42;
    --suit-mid: #24262b;
    --band-navy: rgba(22, 34, 92, 0.88);
    --white: #ffffff;
    --gift-yellow: #f4d21b;
  }
  * { margin: 0; padding: 0; box-sizing: border-box; }
  html, body { width: 750px; height: 1200px; overflow: hidden; background: var(--ink-dark); }
  .cover {
    position: relative;
    width: 750px;
    height: 1200px;
    overflow: hidden;
    color: var(--white);
    font-family: "Noto Sans JP", sans-serif;
  }
  .cover-photo {
    position: absolute;
    inset: 0;
    background:
      radial-gradient(ellipse 55% 45% at 20% 28%, var(--suit-grey) 0%, transparent 70%),
      radial-gradient(ellipse 45% 50% at 88% 55%, var(--suit-mid) 0%, transparent 75%),
      linear-gradient(180deg, #1a1b20 0%, #121317 55%, #0c0d10 100%);
  }
  .vertical { position: absolute; writing-mode: vertical-rl; white-space: nowrap; }
  .upright { text-orientation: upright; }
  .subtitle {
    right: 120px;
    top: 58px;
    font-family: "Noto Serif JP", serif;
    font-weight: 700;
    font-size: 34px;
    letter-spacing: 4px;
    text-shadow: 0 0 6px rgba(0,0,0,0.6);
  }
  .title-line {
    font-weight: 900;
    font-size: 56px;
    line-height: 1;
    letter-spacing: 2px;
    text-shadow: 0 0 8px rgba(0,0,0,0.6);
  }
  .title-line .em { font-size: 72px; }
  .title-line-1 { right: 190px; top: 185px; }
  .title-line-2 { right: 266px; top: 180px; }
  .title-line-3 { right: 352px; top: 178px; }
  .author {
    right: 428px;
    top: 615px;
    font-family: "Noto Serif JP", serif;
    font-weight: 500;
    font-size: 32px;
    letter-spacing: 8px;
  }
  .info-band {
    position: absolute;
    left: 0;
    top: 905px;
    width: 750px;
    height: 295px;
    background: var(--band-navy);
  }
  .lead {
    position: absolute;
    left: 30px;
    top: 26px;
    width: 412px;
    font-size: 19px;
    font-weight: 500;
    line-height: 1.58;
    white-space: nowrap;
  }
  .gift-box {
    position: absolute;
    left: 450px;
    top: 22px;
    width: 282px;
    height: 252px;
    border: 3px solid var(--gift-yellow);
    padding: 10px 14px;
  }
  .gift-heading {
    color: var(--gift-yellow);
    font-size: 28px;
    font-weight: 900;
    text-align: center;
    margin-bottom: 6px;
  }
  .gift-list { list-style: none; font-size: 22px; font-weight: 700; line-height: 1.4; }
  .gift-list li + li { margin-top: 6px; }
</style>
</head>
<body>
  <div class="cover">
    <div class="cover-photo" role="img" aria-label="ダークスーツにネクタイを締めた男性の胸元の写真"></div>

    <p class="vertical subtitle">未来をひらくのは話術より笑顔力</p>

    <h1>
      <span class="vertical title-line title-line-1">どうして<span class="upright">？</span></span>
      <span class="vertical title-line title-line-2"><span class="em">腕時計</span>を<span class="em">磨く</span>と</span>
      <span class="vertical title-line title-line-3"><span class="em">来店客</span>が<span class="em">ふえる</span>のか</span>
    </h1>

    <p class="vertical author">木ノ瀬 遥人</p>

    <section class="info-band">
      <p class="lead">何故、いつも途中で諦めてしまうのか?<br>それは人間の行動の95%は無意識に<br>潜在意識（恒常性維持機能）が<br>働いてしまうことです。<br>それを解決するには、<br>色を味方につけて印象力をアップして<br>信念を書き換えることができれば<br>自分の得たい成果を得ることに気付きました。</p>
      <div class="gift-box">
        <p class="gift-heading">読者プレゼント</p>
        <ol class="gift-list">
          <li>1. 成果を得る為の<br>　5つのステップ</li>
          <li>2. 失敗しないモノ選び<br>マスコミでは出さない<br>モノ選びのポイント</li>
        </ol>
      </div>
    </section>
  </div>
</body>
</html>
```